Visitenkarten-Design für ein Juwelier Geschäft
Zielgruppe
Juwelier Geschäft in modernem offenen design.
Zielgruppe sind kunden und partner/marken
Aufgabenstellung
schlichtes edles Design.
karten sollen später geprägt werden und einen goldschnitt erhalten

```html
<!DOCTYPE html>
<html lang="de">
<head>
<meta charset="utf-8">
<title>Juwelier Brandstein – Visitenkarten</title>
<link rel="stylesheet" href="https://fonts.googleapis.com/css2?family=Poppins:wght@300;400;600;700&display=swap">
<style>
  :root {
    --backdrop: #ebebea;
    --card: #d8cebf;
    --card-edge: #cfc4b4;
    --copper: #b27a52;
    --copper-deep: #9c6641;
    --ink: #4a4540;
  }
  * { margin: 0; padding: 0; box-sizing: border-box; }
  html, body { width: 1200px; height: 418px; overflow: hidden; background: var(--backdrop); }
  body { position: relative; font-family: "Poppins", sans-serif; }

  .card {
    position: absolute;
    top: 73px;
    width: 409px;
    height: 272px;
    background: var(--card);
    border: 1px solid var(--card-edge);
    box-shadow: 0 2px 6px rgba(0,0,0,0.12);
  }
  .card--front { left: 95px; }
  .card--back { left: 696px; }

  .accent-bar {
    position: absolute;
    left: 0;
    width: 7px;
    background: var(--copper);
  }
  .card--front .accent-bar { top: 108px; height: 58px; }
  .card--back .accent-bar { top: 142px; height: 58px; }

  .wordmark {
    position: absolute;
    left: 21px;
    color: var(--copper);
    font-weight: 600;
    line-height: 1;
  }
  .card--front .wordmark { top: 110px; }
  .card--back .wordmark { top: 38px; }
  .wordmark__line-small { display: block; font-size: 17px; letter-spacing: 0.5px; }
  .wordmark__line-large { display: block; font-size: 36px; letter-spacing: 0.5px; margin-top: 2px; }

  .website {
    position: absolute;
    right: 22px;
    bottom: 27px;
    font-size: 11.5px;
    color: var(--ink);
  }

  .person {
    position: absolute;
    left: 21px;
    top: 148px;
    color: var(--copper);
    line-height: 1;
  }
  .person__name { font-size: 25px; font-weight: 300; letter-spacing: 0.3px; }
  .person__role { font-size: 17px; font-weight: 700; color: var(--copper-deep); margin-top: 5px; }

  .contact {
    position: absolute;
    left: 255px;
    top: 172px;
    list-style: none;
    font-size: 10.5px;
    color: var(--ink);
    line-height: 13px;
  }
  .contact__item { display: flex; align-items: flex-start; margin-bottom: 5px; }
  .contact__icon { width: 12px; height: 12px; margin-right: 9px; margin-top: 1px; flex: none; }
</style>
</head>
<body>
  <section class="card card--front" aria-label="Vorderseite">
    <div class="accent-bar"></div>
    <div class="wordmark">
      <span class="wordmark__line-small">JUWELIER</span>
      <span class="wordmark__line-large">BRANDSTEIN</span>
    </div>
    <p class="website">www.brandstein.de</p>
  </section>

  <section class="card card--back" aria-label="Rückseite">
    <div class="wordmark">
      <span class="wordmark__line-small">JUWELIER</span>
      <span class="wordmark__line-large">BRANDSTEIN</span>
    </div>
    <div class="accent-bar"></div>
    <div class="person">
      <p class="person__name">LENA VOGT</p>
      <p class="person__role">DIRECTOR</p>
    </div>
    <ul class="contact">
      <li class="contact__item">
        <svg class="contact__icon" viewBox="0 0 12 12" fill="none" stroke="#4a4540" stroke-width="1">
          <path d="M6 11.2C6 11.2 2 7.2 2 4.6a4 4 0 0 1 8 0C10 7.2 6 11.2 6 11.2z"/>
          <circle cx="6" cy="4.6" r="1.4"/>
        </svg>
        <span>Niederlassung Lingen<br>Lindenallee 14<br>49808 Lingen</span>
      </li>
      <li class="contact__item">
        <svg class="contact__icon" viewBox="0 0 12 12" fill="none" stroke="#4a4540" stroke-width="1">
          <path d="M2.2 1.5l2 0 1 2.6-1.3 1a6 6 0 0 0 3 3l1-1.3 2.6 1v2a1 1 0 0 1-1 1A9 9 0 0 1 1.2 2.5a1 1 0 0 1 1-1z"/>
        </svg>
        <span>+49 0591-204470</span>
      </li>
      <li class="contact__item">
        <svg class="contact__icon" viewBox="0 0 12 12" fill="none" stroke="#4a4540" stroke-width="1">
          <rect x="1" y="2.5" width="10" height="7"/>
          <path d="M1 2.5l5 4 5-4"/>
        </svg>
        <span>info@brandstein.de</span>
      </li>
    </ul>
  </section>
</body>
</html>
```